Business Card Design Project

1. Show the company logo.
2. Only company email ID and website address to be shown (office@zolotoyveter.fm , www.zolotoyveter.fm).
3. Logo to be provided by us, 2 designs just in case. The logo is made with ' Zolotoy Veter' text, need to be edited so that it shows 'Tikhaya Gavan' instead .
4. Single sided business card, portrait or landscape is not a problem; back side to be filled with colors or a design that matches the logo the best.
5. Logo is to be embossed.
6. We're looking at an English and Russian version.
7. any other better idea is always welcomed.

```html
<!DOCTYPE html>
<html lang="en">
<head>
<meta charset="utf-8">
<title>Tikhaya Gavan — Business Card</title>
<link rel="stylesheet" href="https://fonts.googleapis.com/css2?family=Montserrat:wght@700&family=Arimo:wght@700&display=swap">
<style>
  :root {
    --stage-top: #3d4a4a;
    --stage-bottom: #b6bab8;
    --card-dark: #3a4646;
    --brand-blue: #0a5cff;
    --card-white: #ffffff;
    --text-light: #ffffff;
  }
  * { box-sizing: border-box; margin: 0; padding: 0; }
  html, body { width: 1200px; height: 800px; overflow: hidden; }
  body {
    position: relative;
    background: linear-gradient(180deg, var(--stage-top) 0%, var(--stage-bottom) 100%);
  }
  .card {
    position: absolute;
    top: 60px;
    width: 490px;
    height: 688px;
    border-radius: 16px;
    overflow: hidden;
    background: var(--brand-blue);
  }
  .card--front { left: 50px; }
  .card--back { left: 660px; }

  .card__face {
    position: absolute;
    inset: 0;
  }
  .card--front .card__face {
    background: var(--card-dark);
    border-radius: 180px 0 190px 0 / 200px 0 230px 0;
  }
  .card--back .card__face {
    background: var(--card-white);
    border-radius: 180px 0 190px 0 / 200px 0 350px 0;
  }

  .brand-name {
    position: absolute;
    left: 0;
    right: 0;
    top: 290px;
    height: 80px;
    line-height: 80px;
    text-align: center;
    font-family: "Montserrat", sans-serif;
    font-weight: 700;
    font-size: 56px;
    letter-spacing: -1px;
    color: var(--text-light);
    white-space: nowrap;
  }

  .contact {
    position: absolute;
    left: 0;
    right: 0;
    top: 614px;
    text-align: center;
    font-family: "Arimo", sans-serif;
    font-style: normal;
    font-weight: 700;
    font-size: 23px;
    line-height: 28px;
    color: var(--text-light);
  }
</style>
</head>
<body>
  <section class="card card--front" aria-label="Business card front">
    <div class="card__face"></div>
    <p class="brand-name">Tikhaya Gavan</p>
    <address class="contact">
      office@zolotoyveter.fm<br>
      www.zolotoyveter.fm
    </address>
  </section>

  <section class="card card--back" aria-label="Business card back">
    <div class="card__face"></div>
  </section>
</body>
</html>
```